Postcard Design

Books for sale targeting doctors and patients.

Target Market(s)

Medically challenged individuals and doctors

Font styles to use
Serif

Colors

Designer to choose colors to be used in the design.

Requirements
Must have
• see attached
Nice to have
• see attached

```html
<!DOCTYPE html>
<html lang="en">
<head>
<meta charset="utf-8">
<title>A Mending Mind – Postcard</title>
<link rel="stylesheet" href="https://fonts.googleapis.com/css2?family=Carlito:ital,wght@0,400;0,700;1,400;1,700&family=Anton&family=Playfair+Display:ital,wght@0,400;0,700;1,400&family=Oswald:wght@500;700&display=swap">
<style>
  :root {
    --bg-top: #e4edf4;
    --bg-bottom: #d3e2ec;
    --ink: #1d1d1d;
    --headline-blue: #5d9ad6;
    --headline-edge: #2f5f92;
    --cover-red: #c8201d;
    --cover-dark: #2b2330;
    --cover-dusk: #6d4a6a;
    --cover-sky: #bcd3e6;
    --cover-road: #9a8c6a;
    --white: #ffffff;
  }
  * { margin: 0; padding: 0; box-sizing: border-box; }
  html, body { width: 1200px; height: 927px; overflow: hidden; }
  body {
    background: linear-gradient(180deg, var(--bg-top), var(--bg-bottom));
    font-family: "Carlito", "Calibri", sans-serif;
    color: var(--ink);
    position: relative;
  }
  .intro {
    position: absolute; left: 24px; top: 32px; width: 1160px;
    font-style: italic; font-size: 31px; line-height: 50px; white-space: nowrap;
  }
  .cover {
    position: absolute; overflow: hidden;
    box-shadow: 4px 6px 10px rgba(0,0,0,.35);
    text-align: center;
  }
  .cover-art { position: absolute; inset: 0; }
  .cover-one { left: 23px; top: 326px; width: 341px; height: 552px; }
  .cover-one .cover-art {
    background: linear-gradient(180deg, var(--cover-dark) 0%, var(--cover-dusk) 35%, #b86a52 55%, #5a6d4e 75%, #3a3a36 100%);
  }
  .cover-two { left: 371px; top: 326px; width: 356px; height: 552px; border: 3px solid #8aa8c4; }
  .cover-two .cover-art {
    background: linear-gradient(180deg, var(--white) 0%, var(--cover-sky) 28%, #c9a77a 55%, #7f8f54 72%, var(--cover-road) 88%, var(--white) 100%);
  }
  .cover-title { position: relative; color: var(--cover-red); text-transform: uppercase; line-height: 1; }
  .cover-one .cover-title {
    margin-top: 22px; font-family: "Playfair Display", serif; font-weight: 400;
    -webkit-text-stroke: 1.5px var(--white);
  }
  .cover-one .title-small { display: block; font-size: 44px; letter-spacing: 1px; }
  .cover-one .title-big { display: block; font-size: 68px; letter-spacing: 2px; }
  .cover-two .cover-title { font-family: "Oswald", sans-serif; font-weight: 700; margin-top: 24px; }
  .cover-two .title-small { display: block; font-size: 42px; }
  .cover-two .title-big { display: block; font-size: 92px; line-height: .95; }
  .cover-tag { position: absolute; left: 0; right: 0; font-family: "Playfair Display", serif; color: var(--white); }
  .cover-one .cover-tag { bottom: 84px; font-size: 20px; letter-spacing: 2px; }
  .cover-two .cover-tag { top: 250px; font-style: italic; font-size: 38px; text-shadow: 1px 1px 3px rgba(0,0,0,.5); }
  .cover-author {
    position: absolute; left: 0; right: 0; bottom: 20px;
    font-family: "Oswald", sans-serif; font-weight: 500; font-size: 38px;
    color: var(--cover-red);
  }
  .available {
    position: absolute; left: 733px; top: 270px;
    font-family: "Anton", sans-serif; font-weight: 400; font-size: 86px; line-height: 1;
    color: var(--headline-blue); -webkit-text-stroke: 2px var(--headline-edge);
    letter-spacing: 1px;
  }
  .store { position: absolute; font-weight: 700; color: var(--ink); display: flex; align-items: center; gap: 10px; }
  .store-mark { width: 22px; height: 22px; background: var(--ink); border-radius: 50%; }
  .store-pagehouse { left: 746px; top: 372px; font-size: 40px; }
  .store-rivermart { left: 950px; top: 450px; font-size: 48px; }
  .store-inkleaf { left: 740px; top: 528px; font-size: 40px; }
  .review {
    position: absolute; right: 32px; top: 604px;
    font-style: italic; font-size: 23px; line-height: 30px; text-align: right; white-space: nowrap;
  }
  .review-source { position: absolute; right: 32px; top: 758px; font-style: italic; font-size: 22px; }
</style>
</head>
<body>
  <p class="intro">In this remarkable true story, journey along with Mr. Marsh as he overcomes<br>the various challenges and obstacles associated with three brain bleeds over a<br>twenty year period, that constantly attempted to rob him of joy. Learn how to<br>develop a “can-do” attitude in even the most troubling of situations.</p>

  <div class="cover cover-one">
    <div class="cover-art" role="img" aria-label="Book cover artwork: a man seen from behind against a dusky purple and orange sky over fields"></div>
    <h2 class="cover-title"><span class="title-small">A Mending</span><span class="title-big">Mind</span></h2>
    <p class="cover-tag">A TRUE STORY</p>
    <p class="cover-author">DANIEL R. MARSH</p>
  </div>

  <div class="cover cover-two">
    <div class="cover-art" role="img" aria-label="Book cover artwork: a man in a suit walking down a country road toward the horizon under a pale sky"></div>
    <h2 class="cover-title"><span class="title-small">After a Mending</span><span class="title-big">Mind</span></h2>
    <p class="cover-tag">The Road Ahead</p>
    <p class="cover-author">DANIEL R. MARSH</p>
  </div>

  <h1 class="available">AVAILABLE AT</h1>
  <div class="store store-pagehouse">Pagehouse Books</div>
  <div class="store store-rivermart">Rivermart</div>
  <div class="store store-inkleaf"><span class="store-mark"></span>Inkleaf</div>

  <p class="review">“…this tale proves how attitude can<br>turn a life around; even in the most<br>challenging of circumstances… I know<br>it will touch everyone who reads it.”</p>
  <p class="review-source">~ Rivermart Reader Review</p>
</body>
</html>
```